Lawn Maintenance Company needs attractive add for local newspaper

My company Fennick Yard Service offers many lawn and yard services but I want this add to focus on one specific service we offer.
- Lawn Fertilizer and Weed Control -

This will be an add for our local newspaper, likely a 1/4 page

Some more information about this service.
Our customers generally call us when their lawn is over run with weeds or is performing poorly. Most of the time we set them up with a program and we return to their property every 4 - 5 weeks for another application. 95% of our customers return the following year for the same program. If the customer wishes we will also do a one time application

email: fennickyardservice@example.net
phone: call or text 555-418-7390

Target Market(s)

- Local small towns, populations less than 20,000
- Residential and Commercial customers with lawns
- People who are using the competitors service and aren't happy with it

Industry/Entity Type

Lawn Care

Requirements
Must have
• Must include our logo, email address and phone number
• - Logo
• - Email address and phone number (call or text)
• - Must focus on the service we want to sell (fertilizer and weed control)
Nice to have
• Some phrases or words that should be included, does not need to be word for word as long as the point is made
• - We service both Residential & Commercial properties
• - We offer professional service that can dramatically improve your lawn whether you are looking for a single application or a season long fertilizer/weed control program
• - Our lawn techs are licensed and certified applicators
Should not have
• I do not want any stock pictures of people, houses or equipment.

```html
<!DOCTYPE html>
<html lang="en">
<head>
<meta charset="utf-8">
<title>Fennick Yard Service – Lawn Fertilizer and Weed Control</title>
<link rel="stylesheet" href="https://fonts.googleapis.com/css2?family=Open+Sans:wght@400;600;700;800&display=swap">
<style>
  :root {
    --page: #ecebe7;
    --paper: #ffffff;
    --brand-green: #2f8a2b;
    --grass-light: #8ccf3a;
    --grass-mid: #4e9b22;
    --grass-dark: #2d6a14;
    --soil-light: #6b4a33;
    --soil-dark: #3b281b;
    --glove: #d8282b;
    --text-light: #ffffff;
    --phone-yellow: #f7e01f;
  }
  * { box-sizing: border-box; margin: 0; padding: 0; }
  html, body { width: 1200px; height: 800px; overflow: hidden; }
  body {
    background: var(--page);
    font-family: "Open Sans", Arial, sans-serif;
    display: flex;
    align-items: center;
    justify-content: center;
  }
  .ad {
    position: relative;
    width: 620px;
    height: 760px;
    background: var(--paper);
    overflow: hidden;
    box-shadow: 0 2px 10px rgba(0,0,0,0.15);
  }
  .ad-header {
    position: absolute;
    top: 0; left: 0; right: 0;
    height: 190px;
  }
  .brand {
    position: absolute;
    left: 36px;
    top: 96px;
    display: flex;
    align-items: center;
    gap: 12px;
  }
  .brand-mark {
    width: 26px;
    height: 26px;
    background: var(--brand-green);
  }
  .brand-name {
    font-weight: 800;
    font-size: 26px;
    color: var(--brand-green);
    letter-spacing: 0.5px;
    text-transform: uppercase;
  }
  .hand-art {
    position: absolute;
    right: 70px;
    top: 14px;
    width: 120px;
    height: 140px;
    border-radius: 14px;
    background: linear-gradient(160deg, var(--glove) 0%, #a81c1f 55%, var(--grass-mid) 100%);
  }
  .lawn-art {
    position: absolute;
    left: 0; right: 0;
    top: 190px;
    height: 320px;
    background: linear-gradient(180deg, var(--grass-light) 0%, var(--grass-mid) 45%, var(--grass-dark) 100%);
  }
  .soil-art {
    position: absolute;
    left: 0; right: 0;
    top: 510px;
    bottom: 0;
    background: linear-gradient(180deg, var(--soil-light) 0%, var(--soil-dark) 100%);
  }
  .selling-points {
    position: absolute;
    top: 250px;
    left: 40px;
    right: 40px;
    text-align: center;
    color: var(--text-light);
    font-weight: 700;
    font-size: 24px;
    line-height: 1.2;
    text-shadow: 0 2px 4px rgba(0,0,0,0.45);
  }
  .selling-points p + p { margin-top: 22px; }
  .contact {
    position: absolute;
    top: 540px;
    left: 40px;
    right: 40px;
    text-align: center;
    color: var(--text-light);
  }
  .service-title {
    font-weight: 600;
    font-size: 25px;
  }
  .email {
    font-weight: 400;
    font-size: 22px;
    margin-top: 4px;
  }
  .call-label {
    font-weight: 700;
    font-size: 22px;
    margin-top: 16px;
  }
  .phone {
    font-weight: 800;
    font-size: 56px;
    color: var(--phone-yellow);
    letter-spacing: 1px;
    margin-top: 2px;
  }
</style>
</head>
<body>
  <article class="ad">
    <header class="ad-header">
      <div class="brand">
        <span class="brand-mark"></span>
        <span class="brand-name">Fennick Yard Service</span>
      </div>
      <div class="hand-art" role="img" aria-label="Red-gloved hand pulling a weed from the lawn"></div>
    </header>

    <div class="lawn-art" role="img" aria-label="Lush green grass with yellow dandelions"></div>
    <div class="soil-art" role="img" aria-label="Cross-section of dark cracked soil beneath the lawn"></div>

    <section class="selling-points">
      <p>We service both Residential<br>&amp; Commercial properties</p>
      <p>We offer single applications or<br>season long fertilizer/weed control<br>programs</p>
      <p>All of our technicians are certified by<br>Prairie Environment Council</p>
    </section>

    <footer class="contact">
      <p class="service-title">Lawn Fertilizer and Weed Control</p>
      <p class="email">fennickyardservice@example.net</p>
      <p class="call-label">call or text</p>
      <p class="phone">555-418-7390</p>
    </footer>
  </article>
</body>
</html>
```